BRICKWORK BLUEPRINT: THE RELIABLE WAY TO EARN HUGE GAINS FROM BUDGET HOME UPGRADES

I am looking for a book cover design for my new E-Book.

My idea for the design is a pin board with before and after photos of our properties pinned on it (example attached). I have also attached some photos to use.

PLEASE SUBMIT OTHER DESIGNS ALSO AS THIS WAS JUST AN IDEA BUT I AM OPEN TO OTHER IDEAS ALSO.

Page size is 5x7 inches

Font styles to use
Serif
Sans Serif

Colors
0255a3
3176b5
85acd3
85cae6
33a6d7
0392cd
9bcb3c
abd036
ec1f27

```html
<!DOCTYPE html>
<html lang="en">
<head>
<meta charset="utf-8">
<title>Brickwork Blueprint – Book Cover</title>
<link rel="stylesheet" href="https://fonts.googleapis.com/css2?family=Montserrat:wght@400;500;600&display=swap">
<style>
  :root {
    --page: #f2f2f2;
    --paper: #ffffff;
    --ink: #333333;
    --accent: #33a6d7;
    --rule: #9a9a9a;
  }
  html, body {
    margin: 0;
    width: 1034px;
    height: 1200px;
    overflow: hidden;
    background: var(--page);
  }
  .cover {
    position: absolute;
    left: 117px;
    top: 40px;
    width: 800px;
    height: 1120px;
    background: var(--paper);
  }
  .cover svg { display: block; width: 100%; height: 100%; }
  .band { fill: var(--accent); }
  .rule { fill: var(--rule); }
  .title, .subtitle, .author {
    font-family: "Montserrat", sans-serif;
  }
  .title-main { fill: var(--ink); font-weight: 500; font-size: 125px; }
  .title-accent { fill: var(--accent); font-weight: 600; font-size: 100px; }
  .subtitle { fill: var(--ink); font-size: 30px; font-weight: 500; font-variant: small-caps; letter-spacing: 1px; }
  .author { fill: var(--ink); font-size: 56px; font-weight: 500; font-variant: small-caps; letter-spacing: 1px; }
</style>
</head>
<body>
<main class="cover">
  <svg viewBox="0 0 952 1333" xmlns="http://www.w3.org/2000/svg">
    <defs>
      <linearGradient id="before-house" x1="0" y1="0" x2="0" y2="1">
        <stop offset="0" stop-color="#cfd8c9"/>
        <stop offset="1" stop-color="#7e8a6a"/>
      </linearGradient>
      <linearGradient id="navy-house" x1="0" y1="0" x2="0" y2="1">
        <stop offset="0" stop-color="#4b5e8c"/>
        <stop offset="1" stop-color="#1f2a44"/>
      </linearGradient>
      <linearGradient id="lawn-house" x1="0" y1="0" x2="0" y2="1">
        <stop offset="0" stop-color="#7fb6f0"/>
        <stop offset="0.55" stop-color="#d7dad8"/>
        <stop offset="1" stop-color="#5c9a3a"/>
      </linearGradient>
      <linearGradient id="dusk-house" x1="0" y1="0" x2="0" y2="1">
        <stop offset="0" stop-color="#47603b"/>
        <stop offset="0.6" stop-color="#8a8f86"/>
        <stop offset="1" stop-color="#3f6a2c"/>
      </linearGradient>
      <linearGradient id="porch-house" x1="0" y1="0" x2="0" y2="1">
        <stop offset="0" stop-color="#b9aea6"/>
        <stop offset="1" stop-color="#7b6258"/>
      </linearGradient>
    </defs>

    <rect class="band" x="0" y="0" width="952" height="36"/>
    <rect class="rule" x="0" y="36" width="952" height="7"/>

    <text class="title title-main" x="45" y="198" textLength="862" lengthAdjust="spacingAndGlyphs">BRICKWORK</text>
    <text class="title title-accent" x="902" y="303" text-anchor="end">BLUEPRINT</text>

    <g role="img" aria-label="Photo of a two-storey weatherboard house before renovation">
      <polygon points="0,253 300,253 420,477 0,477" fill="url(#before-house)"/>
    </g>
    <g role="img" aria-label="Photo of the same house after renovation, painted navy blue">
      <polygon points="360,367 952,367 952,542 470,542" fill="url(#navy-house)"/>
    </g>
    <g role="img" aria-label="Photo of a renovated grey cottage with white veranda on a green lawn">
      <polygon points="0,477 430,477 680,907 0,907" fill="url(#lawn-house)"/>
    </g>
    <g role="img" aria-label="Photo of a renovated cottage with timber deck under a large tree at dusk">
      <polygon points="470,547 952,547 952,905 680,905" fill="url(#dusk-house)"/>
    </g>
    <g role="img" aria-label="Photo of a weatherboard house entry with porch railing">
      <polygon points="680,907 952,907 952,1145 420,1145" fill="url(#porch-house)"/>
    </g>

    <text class="subtitle">
      <tspan x="47" y="1003">The Reliable Way to</tspan>
      <tspan x="47" y="1041">Earn Huge Gains</tspan>
      <tspan x="47" y="1079">From Budget Home</tspan>
      <tspan x="47" y="1117">Upgrades</tspan>
    </text>

    <text class="author" x="902" y="1235" text-anchor="end">Marcus Whitfield</text>

    <rect class="rule" x="0" y="1295" width="952" height="8"/>
    <rect class="band" x="0" y="1303" width="952" height="30"/>
  </svg>
</main>
</body>
</html>
```